Road Construction Company needs business cards

We would like a new business card designed for our business.

We're a road construction company based in Qld, Australia.

Can the business card please have the following information on it.

Name: Brent Malvoy
Position: General Manager
Phone: 0471 592 304
Email: Brent.malvoy@quendix.com.au
Address: 87 Harrowgate Ave, Pindarra, QLD, 4000
Website: www.quendix.com.au

Visually we'd like the card to be professional and simple.

Attached is our logo.

Our website is www.quendix.com.au

Target Market(s)

Men aged 25-60

Contact Information for Business Card

As listed in project description

Font styles to use
Serif

Requirements
Must have
• Large logo on back of card

```html
<!DOCTYPE html>
<html lang="en">
<head>
<meta charset="utf-8">
<title>Quendix Business Cards</title>
<link rel="stylesheet" href="https://fonts.googleapis.com/css2?family=Poppins:wght@400;500;600;800&display=swap">
<style>
:root{
  --navy:#0b57a4;
  --sky:#31a6d9;
  --white:#ffffff;
  --edge:#e4e4e4;
}
*{margin:0;padding:0;box-sizing:border-box}
html,body{width:1200px;height:1174px;overflow:hidden;background:var(--white)}
body{position:relative;font-family:"Poppins",sans-serif;color:var(--navy)}
.card{position:absolute;width:544px;height:333px;border:1px solid var(--edge);background:var(--white);overflow:hidden}
.col-left{left:22px}
.col-right{left:633px}
.row-1{top:20px}
.row-2{top:419px}
.row-3{top:818px}
.card--navy{background:var(--navy);border-color:var(--navy)}
.abs{position:absolute;white-space:nowrap}
.name{font-size:21px;line-height:1;font-weight:600}
.name .light{font-weight:400}
.role{font-size:14.5px;line-height:1}
.role--sky{color:var(--sky)}
.contact{font-size:14.5px;line-height:1}
.contact--sm{font-size:13.5px}
.sky{color:var(--sky)}
.icon{position:absolute;width:18px;height:18px}
.divider{position:absolute;width:1.5px;background:var(--navy)}
.divider--sky{background:var(--sky);width:2px}
.wordmark{position:absolute;left:0;right:0;text-align:center;font-weight:800;letter-spacing:2px;line-height:1;color:var(--navy)}
.wordmark--lg{font-size:70px}
.wordmark--sm{font-size:40px}
.card--navy .wordmark{color:var(--white)}
.site{position:absolute;left:0;right:0;text-align:center;font-size:14px;line-height:1}
.card--navy .site{color:var(--white)}
.band{position:absolute;bottom:0;height:18px}
.band--sky{left:0;width:204px;background:var(--sky)}
.band--navy{left:204px;right:0;background:var(--navy)}
</style>
</head>
<body>

<svg width="0" height="0" style="position:absolute" aria-hidden="true">
  <symbol id="i-phone" viewBox="0 0 18 18"><rect x="5" y="1" width="9" height="16" rx="1.5" fill="none" stroke="#31a6d9" stroke-width="1.4"/><line x1="8" y1="14.5" x2="11" y2="14.5" stroke="#31a6d9" stroke-width="1.2"/></symbol>
  <symbol id="i-mail" viewBox="0 0 18 18"><rect x="0.5" y="3.5" width="17" height="11" fill="#31a6d9"/><path d="M0.5 3.5 9 10.5 17.5 3.5M0.5 14.5 6.5 8.5M17.5 14.5 11.5 8.5" fill="none" stroke="#fff" stroke-width="1.2"/></symbol>
  <symbol id="i-globe" viewBox="0 0 18 18"><g fill="none" stroke="#31a6d9" stroke-width="1.1"><circle cx="9" cy="9" r="8"/><ellipse cx="9" cy="9" rx="3.6" ry="8"/><line x1="1" y1="9" x2="17" y2="9"/><path d="M2.5 4.8h13M2.5 13.2h13"/></g></symbol>
  <symbol id="i-pin" viewBox="0 0 18 18"><path d="M9 1a6 6 0 0 1 6 6c0 4.5-6 10.5-6 10.5S3 11.5 3 7a6 6 0 0 1 6-6z" fill="#31a6d9"/><circle cx="9" cy="7" r="2.4" fill="#fff"/></symbol>
</svg>

<!-- Front A -->
<section class="card col-left row-1">
  <div class="abs name" style="left:48px;top:134px">Brent Malvoy</div>
  <div class="abs role" style="left:48px;top:156px">General Manager</div>
  <svg class="icon" style="left:50px;top:206px"><use href="#i-phone"/></svg>
  <div class="abs contact" style="left:79px;top:207px">0471 592 304</div>
  <svg class="icon" style="left:50px;top:227px"><use href="#i-mail"/></svg>
  <div class="abs contact" style="left:79px;top:228px">Brent.malvoy@quendix.com.au</div>
  <svg class="icon" style="left:50px;top:248px"><use href="#i-globe"/></svg>
  <div class="abs contact" style="left:79px;top:249px">www.quendix.com.au</div>
  <svg class="icon" style="left:50px;top:269px"><use href="#i-pin"/></svg>
  <div class="abs contact" style="left:79px;top:270px">87 Harrowgate Ave, Pindarra, QLD, 4000</div>
</section>

<!-- Back A -->
<section class="card col-right row-1">
  <div class="wordmark wordmark--lg" style="top:130px">QUENDIX</div>
</section>

<!-- Front B -->
<section class="card col-left row-2">
  <div class="abs name" style="left:48px;top:145px"><span class="light">Brent</span> Malvoy</div>
  <div class="abs role role--sky" style="left:48px;top:168px">General Manager</div>
  <div class="divider" style="left:203px;top:124px;height:78px"></div>
  <svg class="icon" style="left:217px;top:123px"><use href="#i-phone"/></svg>
  <div class="abs contact" style="left:243px;top:124px">0471 592 304</div>
  <svg class="icon" style="left:217px;top:144px"><use href="#i-mail"/></svg>
  <div class="abs contact" style="left:243px;top:145px">Brent.malvoy@quendix.com.au</div>
  <svg class="icon" style="left:217px;top:165px"><use href="#i-globe"/></svg>
  <div class="abs contact" style="left:243px;top:166px">www.quendix.com.au</div>
  <svg class="icon" style="left:217px;top:185px"><use href="#i-pin"/></svg>
  <div class="abs contact contact--sm" style="left:243px;top:187px">87 Harrowgate Ave, Pindarra, QLD, 4000</div>
  <div class="band band--sky"></div>
  <div class="band band--navy"></div>
</section>

<!-- Back B -->
<section class="card card--navy col-right row-2">
  <div class="wordmark wordmark--lg" style="top:130px">QUENDIX</div>
  <div class="site" style="top:272px">www.quendix.com.au</div>
</section>

<!-- Front C -->
<section class="card col-left row-3">
  <div class="wordmark wordmark--sm" style="left:242px;right:auto;top:50px">QUENDIX</div>
  <div class="abs name" style="left:48px;top:226px"><span class="light">BRENT</span> MALVOY</div>
  <div class="abs role role--sky" style="left:48px;top:252px">General Manager</div>
  <div class="divider divider--sky" style="left:223px;top:215px;height:66px"></div>
  <div class="abs contact" style="left:242px;top:209px">0471 592 304</div>
  <div class="abs contact" style="left:242px;top:230px">brent.malvoy@quendix.com.au</div>
  <div class="abs contact sky" style="left:242px;top:251px">www.quendix.com.au</div>
  <div class="abs contact contact--sm" style="left:242px;top:272px">87 Harrowgate Ave, Pindarra, QLD, 4000</div>
</section>

<!-- Back C -->
<section class="card col-right row-3">
  <div class="wordmark wordmark--lg" style="top:130px">QUENDIX</div>
  <div class="site" style="top:272px">WWW.QUENDIX.COM.AU</div>
</section>

</body>
</html>
```